Design a few pages of a luxury magazine for the Prestige Aubergerie Lyon

We need a luxury design for our magazine. See the inDesign pages of the current version attached (zip).

Please work primarily on the first double page (Inventez le luxe de demain) that contains only one photo with legend, a title and the text both in French and English. It must be made clear that the text is the same in two different languages (it is not clear enough here).

You can also work on the other two double pages selected. Feedback will be provided and the 10 best pages will be submitted to a vote at the end of the project timespan.

The most important is a classy and luxury design, this will be printed on expensive paper.

See the full brochure here: https://www.prestigeaubergerie.com/brochure/#page=4

Target Market(s)

Students and parents

Industry/Entity Type

Education

Colors

Designer to choose colors to be used in the design.

Requirements
Must have
• Luxury magazine layout, see:
• https://www.findwerk.com/search?q=luxury+magazine+layout&client=safari&rls=en&source=lnms&tbm=isch&sa=X&ved=0ahUKEwitoIDmit7fAhUVShUIHXC2Cd4Q_AUIDigB&biw=1010&bih=702
Nice to have
• The color of the cover that should be used for blue and grey is #393d49.
• Our font for serif titles (from the logo) is Adobe TRAJAN.
Should not have
• flashy colors

```html
<!DOCTYPE html>
<html lang="fr">
<head>
<meta charset="utf-8">
<title>Inventez le luxe de demain — Prestige Aubergerie Lyon</title>
<link rel="stylesheet" href="https://fonts.googleapis.com/css2?family=Abril+Fatface&family=Josefin+Sans:wght@300;400&family=Fira+Sans:wght@300;400&display=swap">
<style>
  :root {
    --backdrop: #e3e4e6;
    --paper: #ffffff;
    --navy: #2e3442;
    --gold: #c89f6e;
    --gold-soft: #d4b48d;
    --body-ink: #3c3f47;
    --folio: #6a6d74;
  }
  * { box-sizing: border-box; margin: 0; padding: 0; }
  html, body { width: 1200px; height: 1000px; overflow: hidden; }
  body { background: var(--backdrop); position: relative; font-family: "Fira Sans", sans-serif; }

  .spread { position: absolute; left: 0; top: 71px; width: 1157px; height: 735px; display: flex;
            box-shadow: 0 6px 18px rgba(0,0,0,.18); }
  .page { position: relative; width: 578.5px; height: 100%; background: var(--paper); }
  .page--right { border-left: 1px solid #e6e6e6; }

  .hero-photo { position: absolute; left: 0; top: 0; width: 578px; height: 447px;
    background: radial-gradient(ellipse at 50% 30%, #d9b878 0%, #8a6a3c 35%, #3e3222 75%, #241d15 100%); }

  .section-tag { position: absolute; left: 165px; top: 0; width: 247px; height: 47px; background: var(--gold);
    color: #fff; font-family: "Josefin Sans", sans-serif; font-size: 12.5px; letter-spacing: 1.6px;
    display: flex; align-items: center; justify-content: center; padding-top: 3px; }

  .title-block { position: absolute; left: 0; top: 422px; width: 578px; }
  .title-kicker { position: absolute; left: 165px; top: 0; width: 247px; height: 48px; background: var(--gold);
    color: #fff; font-family: "Abril Fatface", serif; font-size: 44px; line-height: 48px; text-align: center; }
  .title-le { position: absolute; left: 128px; top: 58px; font-family: "Josefin Sans", sans-serif; font-weight: 300;
    font-size: 28px; color: var(--navy); letter-spacing: 1px; }
  .title-main { position: absolute; left: 160px; top: 50px; font-family: "Josefin Sans", sans-serif; font-weight: 300;
    font-size: 122px; line-height: 1; color: var(--navy); letter-spacing: 4px; }
  .title-sub { position: absolute; left: 165px; top: 148px; width: 250px; font-family: "Josefin Sans", sans-serif;
    font-weight: 300; font-size: 37px; color: var(--navy); letter-spacing: 4.6px; line-height: 1; white-space: nowrap; }
  .title-rule { position: absolute; left: 165px; top: 198px; width: 247px; height: 1px; background: var(--gold); }
  .title-en { position: absolute; left: 165px; top: 210px; font-family: "Josefin Sans", sans-serif; font-size: 13px;
    color: var(--gold-soft); letter-spacing: 2.4px; line-height: 21px; }

  .folio { position: absolute; top: 697px; width: 100%; text-align: center; font-size: 7px;
    color: var(--folio); letter-spacing: 1px; }

  .bilingual { position: absolute; left: 34px; top: 275px; width: 512px; display: flex; gap: 19px; }
  .column { width: 246px; font-size: 8.3px; line-height: 10.4px; color: var(--body-ink); text-align: justify; }
  .column p + p { margin-top: 6px; }
</style>
</head>
<body>
  <main class="spread">
    <section class="page page--left">
      <div class="hero-photo" role="img" aria-label="Photo de quatre membres de l'équipe pédagogique posant dans le salon doré d'un palace, autour d'une banquette en velours vert"></div>
      <div class="section-tag">À LA PRESTIGE AUBERGERIE</div>
      <div class="title-block">
        <div class="title-kicker">inventez</div>
        <div class="title-le">LE</div>
        <div class="title-main">LUXE</div>
        <div class="title-sub">DE DEMAIN</div>
        <div class="title-rule"></div>
        <div class="title-en">INVENT TOMORROW’S LUXURIES<br>AT THE PRESTIGE AUBERGERIE</div>
      </div>
      <div class="folio">[ 2 ]</div>
    </section>

    <section class="page page--right">
      <div class="bilingual">
        <div class="column column--fr" lang="fr">
          <p>Depuis sa création il y a 30 ans, notre école garde le même objectif : que chaque étudiant acquière les compétences et développe les talents essentiels pour briller dans l’univers du luxe. Première école dédiée à l’hôtellerie de luxe, la Prestige Aubergerie délivre un Bachelor et un Master of Science in International Tourism and Hospitality Management, deux grades universitaires anglais.</p>
          <p>Cette combinaison du luxe à la française et du management anglosaxon donne toutes les clés à nos étudiants pour s’assurer une place privilégiée dans l’univers du luxe en France et à l’international.</p>
          <p>Grâce à l’excellence académique de nos programmes, la dimension internationale de nos formations et l’immersion professionnelle à travers des stages dans les plus prestigieux hôtels du monde, tous nos diplômés sont assurés de faire carrière dans le secteur de leur choix à un poste stratégique. La moitié d’entre eux signent un CDI avant même la fin de leur dernier stage.</p>
        </div>
        <div class="column column--en" lang="en">
          <p>Since its foundation 30 years ago, our school has had only one objective: that each student acquires the skills and develops the essential talents they require to shine within the luxury sector. The Prestige Aubergerie is the first Higher Education establishment dedicated to luxury hotel training; we offer a Bachelor’s and a Master’s degree in International Tourism and Hospitality Management.</p>
          <p>This combination of French-style luxury and Anglo-Saxon management gives our students the key elements they need to ensure a privileged position within the luxury industry both in France and internationally.</p>
          <p>The academic excellence of our programmes, the international dimension of our training and our professional work placements at the most prestigious hotels in the world all ensure that our graduates are certain to secure a career in a strategic role in the luxury sector. Half of our students sign a permanent contract before they even finish their final work placement.</p>
        </div>
      </div>
      <div class="folio">[ 3 ]</div>
    </section>
  </main>
</body>
</html>
```